HVAC&INSULATION Company. Need a website INSULATION targeted.

We are a new HVAC and Insulation company from Washington. (less then 1 year). we already have a website, design, logo etc.. our existing website is targeted for HVAC services.

*** I want to open a 2nd website with a similar design. same logo. same name almost (ORVA INSULATION->ORVA INSULATION)

- our current website is www.orvacleangust.com
i want the new website to be targeted for insulation services

```html
<!DOCTYPE html>
<html lang="en">
<head>
<meta charset="utf-8">
<title>ORVA INSULATION</title>
<link href="https://fonts.googleapis.com/css2?family=Lato:wght@400;700;900&family=Open+Sans:wght@400;700&display=swap" rel="stylesheet">
<style>
  :root {
    --blue: #1a9be0;
    --blue-band: #2aa6e6;
    --navy: #173d63;
    --orange: #fa7a10;
    --ink: #2c3440;
    --text: #555b63;
    --grey-bg: #f1f1f1;
    --line: #d7d7d7;
    --white: #ffffff;
  }
  * { box-sizing: border-box; margin: 0; padding: 0; }
  html, body { width: 1200px; height: 2507px; overflow: hidden; background: var(--white); }
  body { position: relative; font-family: "Lato", sans-serif; color: var(--ink); }

  /* header */
  .site-header { position: absolute; left: 0; top: 0; width: 1200px; height: 95px; background: var(--white); z-index: 5; }
  .nav-link { position: absolute; top: 40px; font: 700 17px "Lato", sans-serif; color: #4a4a4a; letter-spacing: .2px; white-space: nowrap; }
  .brand { position: absolute; left: 490px; top: 12px; width: 220px; text-align: center; }
  .brand-mark { width: 44px; height: 44px; border-radius: 50%; background: var(--blue); margin: 0 auto 5px; }
  .brand-name { font: 900 16px "Lato", sans-serif; color: var(--navy); letter-spacing: .5px; white-space: nowrap; }
  .quote-btn { position: absolute; left: 904px; top: 30px; width: 149px; height: 45px; border-radius: 23px; background: var(--blue); color: var(--white); font: 700 17px "Lato", sans-serif; display: flex; align-items: center; justify-content: center; white-space: nowrap; }

  /* hero */
  .hero-photo { position: absolute; left: 0; top: 95px; width: 1200px; height: 640px;
    background: radial-gradient(ellipse at 65% 45%, #8a6e55 0%, #a37b56 30%, #6d4a2f 70%, #4a3120 100%); }
  .hero-shade { position: absolute; left: 0; top: 95px; width: 1200px; height: 640px; background: rgba(0,0,0,.18); }
  .hero-curve { position: absolute; left: 0; top: 560px; }
  .hero-title { position: absolute; left: 0; top: 272px; width: 1200px; text-align: center; color: var(--white); font: 900 64px/1 "Lato", sans-serif; white-space: nowrap; }
  .hero-sub { position: absolute; left: 0; top: 354px; width: 1200px; text-align: center; color: var(--white); font: 700 44px/1 "Lato", sans-serif; white-space: nowrap; }
  .slide-dot { position: absolute; left: 1044px; width: 14px; height: 14px; border-radius: 50%; background: var(--white); }
  .slide-dot.current { background: transparent; border: 2px solid var(--white); }
  .hero-arrow { position: absolute; top: 635px; }

  .service { position: absolute; top: 536px; width: 268px; height: 268px; border-radius: 50%; background: var(--white); box-shadow: 0 4px 8px rgba(0,0,0,.25); text-align: center; }
  .service.active { background: var(--blue); z-index: 2; }
  .service svg.icon { position: absolute; left: 104px; top: 50px; }
  .service-label { position: absolute; left: 0; top: 130px; width: 268px; font: 700 19px/25px "Lato", sans-serif; color: #333; }
  .service.active .service-label { color: var(--white); }
  .service .chev { position: absolute; left: 116px; top: 202px; }

  /* who we are */
  .who-photo { position: absolute; left: 168px; top: 885px; width: 362px; height: 362px; border-radius: 50%;
    background: radial-gradient(circle at 40% 45%, #c9b57a 0%, #8b7a55 45%, #4e4332 100%); }
  .who-title { position: absolute; left: 593px; top: 900px; font: 700 40px "Lato", sans-serif; color: var(--ink); }
  .who-text { position: absolute; left: 597px; top: 972px; width: 490px; font: 400 16px/23px "Open Sans", sans-serif; color: var(--text); }
  .who-text p + p { margin-top: 23px; }
  .btn-orange { position: absolute; display: flex; align-items: center; justify-content: center; background: var(--orange); color: var(--white); font: 700 16px "Lato", sans-serif; letter-spacing: .5px; }

  /* guarantee */
  .guarantee-photo { position: absolute; left: 0; top: 1262px; width: 1200px; height: 521px;
    background: linear-gradient(120deg, #3fb0ea 0%, #2aa6e6 45%, #1f97d8 100%); }
  .guarantee-curve { position: absolute; left: 0; top: 1258px; }
  .g-title { position: absolute; left: 0; top: 1450px; width: 1200px; text-align: center; color: var(--white); font: 700 40px "Lato", sans-serif; }
  .g-lead { position: absolute; left: 0; top: 1515px; width: 1200px; text-align: center; color: var(--white); font: 700 17px "Open Sans", sans-serif; }
  .g-text { position: absolute; left: 250px; top: 1560px; width: 700px; text-align: center; color: var(--white); font: 400 17px/22px "Open Sans", sans-serif; }
  .btn-navy { position: absolute; left: 506px; top: 1629px; width: 189px; height: 49px; background: var(--navy); color: var(--white); display: flex; align-items: center; justify-content: center; font: 700 19px "Lato", sans-serif; }

  /* newsletter */
  .news-title { position: absolute; left: 144px; top: 1872px; width: 420px; font: 700 33px/42px "Lato", sans-serif; color: var(--blue); }
  .news-text { position: absolute; left: 145px; top: 1972px; width: 400px; font: 400 20px/30px "Open Sans", sans-serif; color: var(--text); }
  .field { position: absolute; left: 578px; width: 448px; height: 47px; background: #f2f2f2; border: 1px solid #c9c9c9; padding-left: 22px; display: flex; align-items: center; font: 400 17px "Open Sans", sans-serif; color: #555; }

  /* partner strip */
  .partners { position: absolute; left: 0; top: 2187px; width: 1200px; height: 129px; background: var(--grey-bg); border-top: 2px solid var(--line); }
  .badge { position: absolute; }

  /* footer */
  .site-footer { position: absolute; left: 0; top: 2316px; width: 1200px; height: 191px; background: var(--navy); }
  .foot-nav { position: absolute; left: 0; top: 46px; width: 1200px; display: flex; justify-content: center; gap: 36px; font: 700 17px "Lato", sans-serif; color: var(--white); }
  .copyright { position: absolute; left: 0; top: 88px; width: 1200px; text-align: center; font: 400 14px "Open Sans", sans-serif; color: var(--white); }
  .social { position: absolute; top: 125px; width: 34px; height: 34px; border-radius: 50%; border: 2px solid var(--white); }
</style>
</head>
<body>

<header class="site-header">
  <span class="nav-link" style="left:180px">OUR TEAM</span>
  <span class="nav-link" style="left:302px">SERVICES</span>
  <span class="nav-link" style="left:409px">REVIEWS</span>
  <div class="brand"><div class="brand-mark"></div><div class="brand-name">ORVA INSULATION</div></div>
  <span class="nav-link" style="left:714px">SAVINGS &amp; SPECIALS</span>
  <span class="quote-btn">GET A QUOTE</span>
</header>

<div class="hero-photo" role="img" aria-label="Installer in a checked shirt fitting insulation between attic rafters"></div>
<div class="hero-shade"></div>
<svg class="hero-curve" width="1200" height="180" viewBox="0 0 1200 180">
  <path d="M0 170 Q600 20 1200 170 L1200 180 L0 180 Z" fill="#ffffff"/>
</svg>
<h1 class="hero-title">ORVA INSULATION</h1>
<p class="hero-sub">WE INSULATE YOUR HOME</p>
<span class="slide-dot current" style="top:300px"></span>
<span class="slide-dot" style="top:323px"></span>
<span class="slide-dot" style="top:345px"></span>
<span class="slide-dot" style="top:367px"></span>
<svg class="hero-arrow" style="left:80px" width="24" height="60" viewBox="0 0 24 60"><path d="M22 2 L2 30 L22 58" fill="none" stroke="#fff" stroke-width="2"/></svg>
<svg class="hero-arrow" style="left:1105px" width="24" height="60" viewBox="0 0 24 60"><path d="M2 2 L22 30 L2 58" fill="none" stroke="#fff" stroke-width="2"/></svg>

<div class="service" style="left:122px">
  <svg class="icon" width="60" height="60" viewBox="0 0 60 60" fill="none" stroke="#1a9be0" stroke-width="2.5"><path d="M4 28 L30 6 L56 28"/><path d="M10 24 V54 H50 V24"/><path d="M18 36 H42 M18 44 H42"/></svg>
  <div class="service-label">ATTIC<br>INSULATION</div>
  <svg class="chev" width="36" height="36" viewBox="0 0 36 36"><circle cx="18" cy="18" r="16" fill="none" stroke="#555" stroke-width="1.5"/><path d="M11 15 L18 22 L25 15" fill="none" stroke="#555" stroke-width="2"/></svg>
</div>
<div class="service" style="left:342px">
  <svg class="icon" width="60" height="60" viewBox="0 0 60 60" fill="none" stroke="#1a9be0" stroke-width="2.5"><rect x="4" y="8" width="52" height="44"/><path d="M4 22 H56 M4 37 H56 M22 8 V22 M40 8 V22 M14 22 V37 M32 22 V37 M48 22 V37 M22 37 V52 M40 37 V52"/></svg>
  <div class="service-label">WALL<br>INSULATION</div>
  <svg class="chev" width="36" height="36" viewBox="0 0 36 36"><circle cx="18" cy="18" r="16" fill="none" stroke="#555" stroke-width="1.5"/><path d="M11 15 L18 22 L25 15" fill="none" stroke="#555" stroke-width="2"/></svg>
</div>
<div class="service active" style="left:588px">
  <svg class="icon" width="60" height="60" viewBox="0 0 60 60" fill="none" stroke="#fff" stroke-width="2.5"><path d="M4 12 H56 M4 48 H56"/><path d="M8 30 C14 20 20 40 26 30 C32 20 38 40 44 30 C48 24 52 30 54 30"/></svg>
  <div class="service-label">CRAWL SPACE<br>INSULATION</div>
  <svg class="chev" width="36" height="36" viewBox="0 0 36 36"><circle cx="18" cy="18" r="16" fill="none" stroke="#fff" stroke-width="1.5"/><path d="M11 15 L18 22 L25 15" fill="none" stroke="#fff" stroke-width="2"/></svg>
</div>
<div class="service" style="left:815px">
  <svg class="icon" width="60" height="60" viewBox="0 0 60 60" fill="none" stroke="#1a9be0" stroke-width="2.5"><path d="M30 4 L56 18 L30 32 L4 18 Z" fill="#1a9be0"/><path d="M4 28 L30 42 L56 28 M4 38 L30 52 L56 38"/></svg>
  <div class="service-label">INSULATION<br>REMOVAL</div>
  <svg class="chev" width="36" height="36" viewBox="0 0 36 36"><circle cx="18" cy="18" r="16" fill="none" stroke="#555" stroke-width="1.5"/><path d="M11 15 L18 22 L25 15" fill="none" stroke="#555" stroke-width="2"/></svg>
</div>

<div class="who-photo" role="img" aria-label="Worker in a hard hat and safety vest installing insulation"></div>
<h2 class="who-title">WHO WE ARE</h2>
<div class="who-text">
  <p>ORVA INSULATION is a local and family owned company. We provide high quality insulation services with excellent customer satisfaction in the greater Marrowby, WA area.</p>
  <p>We help families keep their homes warm, improve their home life and reduce their energy bills. We're committed to being a company and service that you trust.</p>
</div>
<span class="btn-orange" style="left:593px;top:1156px;width:171px;height:42px">READ MORE</span>

<div class="guarantee-photo" role="img" aria-label="Happy family relaxing together in a warm home, tinted blue"></div>
<svg class="guarantee-curve" width="1200" height="90" viewBox="0 0 1200 90">
  <path d="M0 0 L1200 0 L1200 8 Q600 110 0 8 Z" fill="#ffffff"/>
  <path d="M0 8 Q600 110 1200 8" fill="none" stroke="#173d63" stroke-width="8"/>
</svg>
<h2 class="g-title">OUR GUARANTEE</h2>
<p class="g-lead">That is why we offer a 100% satisfaction guarantee on every project!</p>
<p class="g-text">massa libero interdum nec interdum vel blandit sed nulla in ullamcorper est eget tempor cursus neque mi consectetuer mi a ultricies massa est</p>
<span class="btn-navy">READ MORE</span>

<h2 class="news-title">GET 1 EMAIL EVERY 3 MONTHS &amp; SAVE MONEY!</h2>
<p class="news-text">Save up to 50% off! We promise, ONE email every three months.</p>
<div class="field" style="top:1853px">First Name</div>
<div class="field" style="top:1910px">Last Name</div>
<div class="field" style="top:1968px">Email address</div>
<span class="btn-orange" style="left:580px;top:2029px;width:177px;height:43px;font-size:19px">SUBMIT</span>

<div class="partners">
  <svg class="badge" style="left:196px;top:16px" width="100" height="96" viewBox="0 0 100 96" role="img" aria-label="Partner award badge"><circle cx="50" cy="48" r="44" fill="#f47b20"/></svg>
  <svg class="badge" style="left:390px;top:32px" width="160" height="62" viewBox="0 0 160 62" role="img" aria-label="Accreditation badge"><rect width="160" height="62" rx="6" fill="#1d4f7c"/></svg>
  <svg class="badge" style="left:640px;top:30px" width="160" height="66" viewBox="0 0 160 66" role="img" aria-label="Review listing badge"><rect width="160" height="66" rx="8" fill="#c8201e"/></svg>
  <svg class="badge" style="left:916px;top:20px" width="84" height="84" viewBox="0 0 84 84" role="img" aria-label="Business listing badge"><rect width="84" height="84" rx="10" fill="#3b74d8"/></svg>
</div>

<footer class="site-footer">
  <nav class="foot-nav"><span>OUR TEAM</span><span>SERVICES</span><span>REVIEWS</span><span>SAVINGS &amp; SPECIALS</span><span>GET A QUOTE</span></nav>
  <p class="copyright">© 2018 Company Name&nbsp; All right reserved</p>
  <span class="social" style="left:543px" aria-label="Social link"></span>
  <span class="social" style="left:584px" aria-label="Social link"></span>
  <span class="social" style="left:625px" aria-label="Social link"></span>
</footer>

</body>
</html>
```